Pull Up Banner - Recruitment Company

We would like a design for a pull up banner.

For context: we are a recruitment business. We specialise in helping people in healthcare industry to find jobs in Australia.

I have come up with several ideas and text for the banner. Feel free to use the following as you see appropriate:

- Our logo (see attached)
- 'Healthcare Recruitment Agency'
- Some sort of imagine / cartoon of medical professionals (ie. doctor, nurse, physiotherapist, speech pathologist). A cartoon is more friendly than committing to a photo
- 'Empowering your next career move'
- 'Discover tailored opportunities based on your career preferences'
- Dot points (allied health, nursing, medical imaging)
- Contact info at the bottom including our website (www.quellstaffing.com.au, our Instagram handle @quellstaffing, Mobile: XXXX XXX XXX. The title section for contact information could be 'Get in touch:'

Feel free to submit a couple of designs and we can merge aspects that look good on your designs and find the perfect fit.
Thank you
Updates

Hello,

Thank you for your initial submissions to this project. I appreciate the time you've invested.

After reviewing the first attempt, I'd like to share some feedback and initial observations:

- Professionalism and engagement: Is the overall appearance of the banner professional? It's crucial that we have a high-quality design as this will represent our business.

- Image selection: The image (whether cartoon or real people) appears quite generic. Please consider submitting the banner with a few different photos in the middle for us to choose from. Ensure the image is a good fit and not simply a generic stock photo.

- Contact section: Kindly remove the phone number; we no longer wish to include it on the banner. Instead, please include our website (www.quellstaffing.com.au) and Instagram handle (@quellstaffing).

- Color scheme: White, black, and red/pink are preferred, or alternatively, blue. However, please avoid incorporating too many different colors as it may detract from the professional appearance.

We will be printing the design on a banner and require it to look professional and engaging.

Thank you once again for your submissions. I hope the feedback provided above is helpful.

Warm regards,

Target Market(s)

Allied Health Australia

Font styles to use
Serif

Colors
0054AA
0677BA
7BADD7
CADEEF
E8F1F8
0094D4
00A9DD
6FCCEA
C7EBF8
E9F6FB
EB3D1F
EC4F4E
F09395
F8D3D4
FCEDEE

```html
<!DOCTYPE html>
<html lang="en">
<head>
<meta charset="utf-8">
<title>Quell Staffing – Pull Up Banner</title>
<link href="https://fonts.googleapis.com/css2?family=Montserrat:wght@300;400;500;600;700;800;900&display=swap" rel="stylesheet">
<style>
  :root {
    --pink: #e2446c;
    --pink-soft: #f48ea1;
    --pink-light: #f7a3b1;
    --teal: #7dd3d3;
    --teal-deep: #5cc4c4;
    --ink: #1d1d24;
    --paper: #f6f6f7;
    --grey-band: #e6e6e8;
    --stage: #eef1f4;
    --white: #ffffff;
  }
  * { margin: 0; padding: 0; box-sizing: border-box; }
  html, body { width: 1200px; height: 1200px; overflow: hidden; }
  body {
    background: var(--stage);
    font-family: "Montserrat", sans-serif;
    position: relative;
  }
  .banner {
    position: absolute;
    left: 370px; top: 20px;
    width: 460px; height: 1160px;
    background: var(--paper);
    overflow: hidden;
    box-shadow: 0 10px 30px rgba(0,0,0,0.08);
  }
  .header-wave { position: absolute; left: 0; top: 0; width: 460px; height: 130px; }
  .brand {
    position: absolute; left: 26px; top: 60px;
    display: flex; align-items: center; gap: 8px;
    color: var(--white); font-weight: 700; font-size: 22px; letter-spacing: 1px;
  }
  .brand-dot { width: 8px; height: 8px; background: var(--white); border-radius: 50%; }
  .headline { position: absolute; left: 30px; top: 128px; line-height: 1; }
  .headline .line-1 { font-weight: 800; font-size: 36px; color: var(--ink); letter-spacing: -0.5px; }
  .headline .line-2 { font-weight: 800; font-size: 38px; color: var(--pink); letter-spacing: -0.5px; }
  .headline .line-3 { font-weight: 400; font-size: 26px; color: var(--ink); margin-top: 2px; letter-spacing: -0.5px; }
  .headline-rule { display: flex; gap: 4px; margin-top: 6px; }
  .headline-rule span { height: 3px; display: block; }
  .headline-rule .r1 { width: 110px; background: var(--pink); }
  .headline-rule .r2 { width: 30px; background: var(--ink); }
  .hero {
    position: absolute; left: 220px; top: 230px;
    width: 290px; height: 290px; border-radius: 50%;
    background: radial-gradient(circle at 45% 40%, #8fdada, var(--teal-deep));
  }
  .specialties { position: absolute; left: 0; top: 392px; list-style: none; }
  .specialties li {
    height: 36px; margin-bottom: 12px;
    background: var(--teal);
    border-radius: 0 10px 10px 0;
    display: flex; align-items: center; padding-left: 22px;
    font-weight: 700; font-size: 15px; color: var(--ink);
  }
  .specialties li::before {
    content: ""; width: 5px; height: 5px; border-radius: 50%;
    background: var(--ink); margin-right: 7px;
  }
  .specialties li:nth-child(1) { width: 180px; }
  .specialties li:nth-child(2) { width: 200px; }
  .specialties li:nth-child(3) { width: 228px; }
  .tagline { position: absolute; left: 0; top: 588px; width: 460px; text-align: center; }
  .tagline .lead { font-weight: 700; font-size: 24px; color: var(--ink); letter-spacing: 0.2px; }
  .tagline .career {
    font-weight: 900; font-size: 86px; line-height: 0.95;
    color: var(--pink); letter-spacing: -4px; margin-top: 2px;
  }
  .move-band {
    position: absolute; left: 0; top: 708px; width: 460px; height: 92px;
    background: linear-gradient(90deg, var(--pink-soft), var(--pink));
    display: flex; align-items: center; justify-content: center;
    color: var(--white); font-weight: 800; font-size: 62px; letter-spacing: 26px; padding-left: 26px;
  }
  .intro-band {
    position: absolute; left: 0; top: 845px; width: 460px; height: 112px;
    background: linear-gradient(90deg, var(--grey-band), #f1f1f2 50%, var(--grey-band));
    display: flex; align-items: center; justify-content: center; text-align: center;
    font-weight: 600; font-size: 19px; line-height: 1.25; color: #3a3a40;
  }
  .contact { position: absolute; left: 0; top: 985px; width: 460px; height: 175px; }
  .contact-wave { position: absolute; left: 0; top: 0; width: 460px; height: 175px; }
  .contact-title {
    position: absolute; left: 0; top: 28px;
    background: var(--white); border-radius: 0 18px 18px 0;
    padding: 7px 18px 7px 22px;
    font-weight: 600; font-size: 16px; color: #333; letter-spacing: 0.5px;
  }
  .contact-list { position: absolute; left: 22px; top: 78px; list-style: none; }
  .contact-list li {
    display: flex; align-items: center; gap: 10px;
    color: var(--white); font-size: 13px; font-weight: 500; height: 26px;
  }
  .contact-list svg { width: 18px; height: 18px; }
  .contact-rule {
    position: absolute; left: 22px; right: 22px; bottom: 14px;
    height: 2px; background: var(--white);
  }
</style>
</head>
<body>
  <main class="banner">
    <svg class="header-wave" viewBox="0 0 460 130" preserveAspectRatio="none" aria-hidden="true">
      <path d="M0 0 H460 V20 C330 40 160 80 0 125 Z" fill="var(--pink)"/>
      <path d="M0 125 C160 80 330 40 460 20 V30 C330 52 160 92 0 130 Z" fill="#ffffff" opacity="0.6"/>
    </svg>
    <div class="brand"><span class="brand-name">QUELL</span><span class="brand-dot"></span></div>

    <header class="headline">
      <div class="line-1">HEALTHCARE</div>
      <div class="line-2">RECRUITMENT</div>
      <div class="line-3">AGENCY</div>
      <div class="headline-rule"><span class="r1"></span><span class="r2"></span></div>
    </header>

    <div class="hero" role="img" aria-label="Friendly cartoon doctor in a white coat with a stethoscope, pointing up, set in a teal circle"></div>

    <ul class="specialties">
      <li>ALLIED HEALTH</li>
      <li>NURSING</li>
      <li>MEDICAL IMAGING</li>
    </ul>

    <section class="tagline">
      <div class="lead">EMPOWERING YOUR NEXT</div>
      <div class="career">CAREER</div>
    </section>
    <div class="move-band">MOVE</div>

    <p class="intro-band">Discover tailored opportunities<br>based on your career preferences</p>

    <footer class="contact">
      <svg class="contact-wave" viewBox="0 0 460 175" preserveAspectRatio="none" aria-hidden="true">
        <path d="M0 10 C150 0 320 10 460 40 V175 H0 Z" fill="var(--pink-light)"/>
        <path d="M0 10 C150 0 320 10 460 40 V48 C320 20 150 10 0 20 Z" fill="#ffffff" opacity="0.7"/>
      </svg>
      <div class="contact-title">GET IN TOUCH</div>
      <ul class="contact-list">
        <li>
          <svg viewBox="0 0 18 18" aria-hidden="true"><circle cx="9" cy="9" r="9" fill="#fff"/><path d="M6 4.5 L7.6 4.5 L8.3 7 L7.3 7.8 C7.8 9 8.9 10.1 10.2 10.7 L11 9.7 L13.5 10.4 V12 C13.5 12.8 12.8 13.5 12 13.4 C8.5 13 5 9.5 4.6 6 C4.5 5.2 5.2 4.5 6 4.5Z" fill="var(--pink)"/></svg>
          +61 4000 1111 22
        </li>
        <li>
          <svg viewBox="0 0 18 18" aria-hidden="true"><circle cx="9" cy="9" r="9" fill="#fff"/><circle cx="9" cy="9" r="3" fill="var(--pink)"/></svg>
          @quellstaffing
        </li>
        <li>
          <svg viewBox="0 0 18 18" aria-hidden="true"><circle cx="9" cy="9" r="9" fill="#fff"/><g fill="none" stroke="var(--pink)" stroke-width="1.1"><circle cx="9" cy="9" r="5"/><ellipse cx="9" cy="9" rx="2.2" ry="5"/><path d="M4 9 H14"/></g></svg>
          www.quellstaffing.com.au
        </li>
      </ul>
      <div class="contact-rule"></div>
    </footer>
  </main>
</body>
</html>
```